Animal Eye Clinic needs a Business card

We are a new veterinary ophthalmology practice (Silverbrook Pet Vision Care) and we need a business card designed. We only see animal eyes - we are not a regular veterinary clinic. We already have a logo. We are looking for a professional, good looking business card to hand out to our clients. We are looking for something simple but professional and contemporary. Our logo is likely the only picture/graphic that needs to be on the card.

Contact Information for Business Card

Marisol Quent, BSc, DVM, MSc, DipACVO
Veterinary Ophthalmologist

Phone: 250.419.3067
Email: silverbrookpetvisioncare@mailvero.com
Website: silverbrookpetvisioncare.com
Address: 1875 Tessock Rd
Kelowna, BC, V4T 8M3

Colors

Designer to choose colors to be used in the design.

Requirements
Must have
• Our logo (attached)

```html
<!DOCTYPE html>
<html lang="en">
<head>
<meta charset="utf-8">
<title>Silverbrook Pet Vision Care — Business Card</title>
<link rel="stylesheet" href="https://fonts.googleapis.com/css2?family=Montserrat:wght@400;500;600&display=swap">
<style>
  :root {
    --teal: #0f97a7;
    --ink: #1b1b1b;
    --grey: #6a6a6a;
    --paper: #ffffff;
    --page: #ffffff;
  }
  * { box-sizing: border-box; margin: 0; padding: 0; }
  html, body {
    width: 1200px; height: 1200px; overflow: hidden;
    background: var(--page);
    font-family: "Montserrat", Arial, sans-serif;
  }
  .canvas { position: relative; width: 1200px; height: 1200px; }

  .card {
    position: absolute;
    box-shadow: 0 2px 8px rgba(0,0,0,0.28);
  }
  .card-front {
    left: 183px; top: 81px; width: 841px; height: 480px;
    background: var(--ink);
    display: flex; align-items: center; justify-content: center;
  }
  .front-brand {
    display: flex; align-items: center; gap: 22px;
    color: var(--teal); font-weight: 600; font-size: 34px; line-height: 1.15;
  }
  .brand-dot {
    width: 96px; height: 96px; border-radius: 50%;
    background: var(--teal); flex: none;
  }

  .card-back {
    left: 186px; top: 625px; width: 835px; height: 476px;
    background: var(--paper);
  }
  .back-brand {
    position: absolute; left: 30px; top: 69px;
    display: flex; align-items: center; gap: 18px;
    color: var(--teal); font-weight: 600; font-size: 32px; line-height: 1.12;
  }
  .back-brand .brand-dot { width: 74px; height: 74px; }

  .person { position: absolute; left: 30px; top: 246px; }
  .person-name {
    color: var(--teal); font-weight: 600; font-size: 35px;
    letter-spacing: 0.5px; line-height: 1;
  }
  .person-meta {
    margin-top: 6px; color: var(--grey); font-size: 19.5px; line-height: 27px;
  }

  .divider {
    position: absolute; left: 30px; top: 347px; width: 776px; height: 2px;
    background: var(--teal);
  }

  .contact-list {
    position: absolute; left: 30px; top: 362px; list-style: none;
  }
  .contact-list li {
    display: flex; align-items: center; gap: 12px;
    height: 30px; color: var(--grey); font-size: 19px;
  }
  .contact-list svg { width: 20px; height: 20px; flex: none; }

  .address {
    position: absolute; right: 29px; top: 360px; text-align: right;
    color: var(--grey); font-size: 19px; line-height: 30px;
  }
  .address-company {
    color: var(--teal); font-weight: 600; font-size: 19px; letter-spacing: 0.6px;
  }
</style>
</head>
<body>
<main class="canvas">
  <section class="card card-front" aria-label="Card front">
    <div class="front-brand">
      <span class="brand-dot" aria-hidden="true"></span>
      <span>Silverbrook<br>Pet Vision Care</span>
    </div>
  </section>

  <section class="card card-back" aria-label="Card back">
    <div class="back-brand">
      <span class="brand-dot" aria-hidden="true"></span>
      <span>Silverbrook<br>Pet Vision Care</span>
    </div>

    <div class="person">
      <h1 class="person-name">MARISOL QUENT</h1>
      <p class="person-meta">BSc, DVM, MSc, DipACVO<br>Veterinary Ophthalmologist</p>
    </div>

    <div class="divider"></div>

    <ul class="contact-list">
      <li>
        <svg viewBox="0 0 24 24" aria-hidden="true"><path fill="#0f97a7" d="M6.6 10.8a15.1 15.1 0 0 0 6.6 6.6l2.2-2.2a1 1 0 0 1 1-.25 11.4 11.4 0 0 0 3.6.57 1 1 0 0 1 1 1V20a1 1 0 0 1-1 1A17 17 0 0 1 3 4a1 1 0 0 1 1-1h3.5a1 1 0 0 1 1 1c0 1.25.2 2.45.57 3.57a1 1 0 0 1-.25 1z"/><path fill="none" stroke="#0f97a7" stroke-width="1.8" stroke-linecap="round" d="M14 3.5a6.5 6.5 0 0 1 6.5 6.5M14 7a3 3 0 0 1 3 3"/></svg>
        <span>250.419.3067</span>
      </li>
      <li>
        <svg viewBox="0 0 24 24" aria-hidden="true"><rect x="1.5" y="5" width="21" height="14" fill="#0f97a7"/><path d="M2 5.5l10 7.5 10-7.5M2 18.5l7.5-6.5M22 18.5l-7.5-6.5" fill="none" stroke="#fff" stroke-width="1.5"/></svg>
        <span>silverbrookpetvisioncare@mailvero.com</span>
      </li>
      <li>
        <svg viewBox="0 0 24 24" aria-hidden="true"><circle cx="12" cy="12" r="10.5" fill="#0f97a7"/><path d="M1.5 12h21M12 1.5c3 3 3 18 0 21M12 1.5c-3 3-3 18 0 21" fill="none" stroke="#fff" stroke-width="1.3"/></svg>
        <span>www.silverbrookpetvisioncare.com</span>
      </li>
    </ul>

    <address class="address" style="font-style:normal">
      <div class="address-company">SILVERBROOK PET VISION CARE</div>
      <div>1875 Tessock Rd</div>
      <div>Kelowna, BC, V4T 8M3</div>
    </address>
  </section>
</main>
</body>
</html>
```